Vintage Infographic Background Design

I need an infographic which has a vintage background design. The file "Infographic Background Design Primer" describes the nature of the design required. Thank you for taking the time to read this and I look forward to working with you.
Target Market(s)
Law Students
Industry/Entity Type
Law Firm
Font styles to use
Serif
Script
Colors
fece3e
ffcf3e
fbf289
f37122
f04a50
f59195
fee3d4
fbe7d2
fee18a
Requirements
Must have
- All three tasks mentioned in the "Infographic Background Design Primer" uploaded on 20th May 2016.
Should not have
- The infographic should not convey the impression that it is tacky/run of the mill.

```html
<!DOCTYPE html>
<html lang="fr">
<head>
<meta charset="utf-8">
<title>Lorem ipsum – infographie</title>
<link href="https://fonts.googleapis.com/css2?family=Great+Vibes&family=Lora:ital,wght@0,400;0,600;1,400&display=swap" rel="stylesheet">
<style>
  :root {
    --maroon: #5a1d2b;
    --maroon-deep: #43121e;
    --cream: #f3e2c4;
    --seal-light: #8a2d2d;
    --seal-dark: #5c1818;
    --backdrop: #f4ecdc;
  }
  * { box-sizing: border-box; margin: 0; padding: 0; }
  html, body { width: 853px; height: 1200px; overflow: hidden; background: var(--backdrop); }
  .infographic {
    position: relative; width: 853px; height: 1200px; overflow: hidden;
    font-family: "Lora", Georgia, serif; color: var(--cream);
  }
  .parchment { position: absolute; inset: 0; }

  .gavel-icon {
    position: absolute; top: 100px; width: 56px; height: 42px;
    background: var(--maroon); border-radius: 6px;
  }
  .gavel-icon--left { left: 128px; }
  .gavel-icon--right { right: 128px; }

  .headline {
    position: absolute; top: 66px; left: 0; width: 100%; text-align: center;
    font-family: "Great Vibes", cursive; font-weight: 400;
    font-size: 92px; line-height: 1; color: var(--maroon);
  }
  .tagline {
    position: absolute; top: 176px; left: 0; width: 100%; text-align: center;
    font-size: 21px; letter-spacing: 1px; color: var(--maroon);
  }

  .panel { position: absolute; background: var(--maroon); box-shadow: 0 2px 6px rgba(60, 20, 20, .35); }
  .panel-copy {
    font-size: 12px; line-height: 1.55; text-transform: uppercase;
    text-align: center; letter-spacing: .3px;
  }
  .panel--intro { left: 108px; top: 220px; width: 637px; height: 150px; padding: 24px 40px; }

  .scales-badge {
    position: absolute; left: 630px; top: 338px; width: 112px; height: 112px;
    border-radius: 50%; background: var(--maroon);
  }
  .scales-badge span {
    position: absolute; left: 30px; top: 28px; width: 52px; height: 54px;
    border-radius: 8px; background: var(--cream); opacity: .85;
  }

  .advocate-figure {
    position: absolute; left: 46px; top: 400px; width: 224px; height: 260px;
    background: linear-gradient(180deg, #6a2433, var(--maroon-deep));
    border-radius: 80px 80px 6px 6px;
  }
  .lectern { left: 57px; top: 656px; width: 182px; height: 262px; padding: 96px 14px 12px; }
  .quill-badge {
    position: absolute; left: 59px; top: 18px; width: 64px; height: 64px;
    border-radius: 50%; background: var(--cream);
  }
  .lectern .panel-copy { font-size: 11px; line-height: 1.5; }

  .stat-label { position: absolute; font-size: 17px; font-style: italic; color: var(--maroon); }
  .stat-dot {
    position: absolute; border-radius: 50%; background: var(--maroon);
    display: flex; align-items: center; justify-content: center; text-align: center;
  }
  .stat-dot p { font-size: 8px; line-height: 1.3; text-transform: uppercase; width: 70%; }
  .stat-hub { padding: 0 12px; flex-direction: column; }
  .stat-hub strong {
    display: block; font-family: "Great Vibes", cursive; font-weight: 400;
    font-size: 32px; line-height: 1;
  }
  .stat-hub p { font-size: 8.5px; width: 100%; }

  .panel--facts { left: 270px; top: 700px; width: 525px; height: 160px; padding: 58px 30px 12px; }
  .panel-title {
    position: absolute; left: 0; top: 8px; width: 100%; text-align: center;
    font-family: "Great Vibes", cursive; font-weight: 400; font-size: 42px; line-height: 1; color: var(--cream);
  }

  .section-title--agreement {
    position: absolute; left: 340px; width: 300px; top: 924px; text-align: center;
    font-family: "Great Vibes", cursive; font-weight: 400; font-size: 42px; line-height: 1; color: var(--maroon);
  }
  .panel--agreement { left: 156px; top: 975px; width: 484px; height: 147px; padding: 14px 24px 14px 196px; }
  .panel--agreement .panel-copy { font-size: 11px; line-height: 1.45; }
  .handshake-badge {
    position: absolute; left: 171px; top: 937px; width: 170px; height: 170px;
    border-radius: 50%; background: var(--cream); border: 12px solid var(--maroon);
  }
  .seal {
    position: absolute; left: 640px; top: 1010px; width: 100px; height: 100px;
    border-radius: 50%; background: radial-gradient(circle, var(--seal-light), var(--seal-dark));
  }
</style>
</head>
<body>
<main class="infographic">
  <svg class="parchment" width="853" height="1200" viewBox="0 0 853 1200" aria-hidden="true">
    <defs>
      <radialGradient id="paperTone" cx="50%" cy="45%" r="70%">
        <stop offset="0%" stop-color="#f1dcb2"/>
        <stop offset="65%" stop-color="#e2bf88"/>
        <stop offset="100%" stop-color="#b98249"/>
      </radialGradient>
    </defs>
    <path d="M22 28 L110 18 L200 30 L320 16 L430 26 L560 14 L690 28 L830 20 L840 140 L828 300 L842 460 L832 640 L845 820 L834 1000 L842 1180 L700 1188 L560 1178 L420 1190 L280 1180 L140 1190 L16 1182 L26 1000 L12 820 L24 640 L10 460 L22 300 L12 140 Z"
          fill="url(#paperTone)" stroke="#a8733f" stroke-width="3"/>
    <g stroke="#5a1d2b" stroke-width="2">
      <line x1="560" y1="520" x2="471" y2="462"/>
      <line x1="560" y1="520" x2="693" y2="505"/>
      <line x1="560" y1="520" x2="450" y2="592"/>
      <line x1="560" y1="520" x2="693" y2="640"/>
    </g>
  </svg>

  <div class="gavel-icon gavel-icon--left" role="img" aria-label="Icône de marteau de juge"></div>
  <div class="gavel-icon gavel-icon--right" role="img" aria-label="Icône de marteau de juge"></div>

  <h1 class="headline">Lorem ipsum</h1>
  <p class="tagline">LOREM IPSUM, EST UN FAUX TEXTE</p>

  <section class="panel panel--intro">
    <p class="panel-copy">Le Lorem Ipsum est simplement du faux texte employé dans la composition et la mise en page avant impression. Le Lorem Ipsum est le faux texte standard de l'imprimerie depuis les années 1500, quand un imprimeur anonyme assembla ensemble des morceaux de texte pour réaliser un livre spécimen de polices de texte.</p>
  </section>

  <div class="scales-badge"><span role="img" aria-label="Icône de balance de la justice"></span></div>

  <div class="advocate-figure" role="img" aria-label="Silhouette d'un avocat en robe plaidant"></div>

  <section class="panel lectern">
    <div class="quill-badge" role="img" aria-label="Icône de plume"></div>
    <p class="panel-copy">Le Lorem Ipsum est simplement du faux texte employé dans la composition et la mise en page. Le Lorem Ipsum est le faux texte standard.</p>
  </section>

  <span class="stat-label" style="left:452px;top:408px">15%</span>
  <div class="stat-dot" style="left:443px;top:434px;width:56px;height:56px"></div>

  <span class="stat-label" style="left:408px;top:548px">15%</span>
  <div class="stat-dot" style="left:416px;top:558px;width:68px;height:68px"></div>

  <div class="stat-dot stat-hub" style="left:500px;top:460px;width:120px;height:120px">
    <strong>Stat</strong>
    <p>Le Lorem Ipsum est simplement du faux texte.</p>
  </div>

  <span class="stat-label" style="left:734px;top:452px">15%</span>
  <div class="stat-dot" style="left:657px;top:469px;width:72px;height:72px">
    <p>Le Lorem Ipsum est simplement.</p>
  </div>

  <span class="stat-label" style="left:735px;top:578px">45%</span>
  <div class="stat-dot" style="left:647px;top:594px;width:92px;height:92px">
    <p>Le Lorem Ipsum est simplement du faux.</p>
  </div>

  <section class="panel panel--facts">
    <h2 class="panel-title">Title goes here</h2>
    <p class="panel-copy">Le Lorem Ipsum est simplement du faux texte employé dans la composition et la mise en page avant impression. Le Lorem Ipsum est le faux texte standard de l'imprimerie depuis les années 1500, quand un imprimeur anonyme assembla des morceaux de texte.</p>
  </section>

  <h2 class="section-title--agreement">Title goes here</h2>
  <section class="panel panel--agreement">
    <p class="panel-copy">Le Lorem Ipsum est simplement du faux texte employé dans la composition et la mise en page avant impression. Le Lorem Ipsum est le faux texte standard de l'imprimerie depuis les années 1500.</p>
  </section>
  <div class="handshake-badge" role="img" aria-label="Icône de poignée de main"></div>
  <div class="seal" role="img" aria-label="Sceau de cire rouge"></div>
</main>
</body>
</html>
```